Redesign Website Homepage Header

We are looking for a re-design of the header section of our website homepage. The style of the website, image assets and copy can all remain the same, but we want an alternative layout that matches the rest of the website. Full brief attached.

Reason: Project has been launched over a weekend so might have low response. Extending to cover more working week days.

```html
<!DOCTYPE html>
<html lang="en">
<head>
<meta charset="utf-8">
<title>SkyDesk – Hosted Desktops for IT Resellers</title>
<link href="https://fonts.googleapis.com/css2?family=Lato:wght@400;700;900&display=swap" rel="stylesheet">
<style>
:root{
  --navy:#0d4b72;
  --navy-text:#16496f;
  --coral:#ef4f57;
  --white:#ffffff;
  --hero-a:#9fbcbf;
  --hero-b:#c6d9d8;
  --wood:#7a5a43;
  --lower-a:#8d8c89;
  --lower-b:#c9c4bd;
}
*{margin:0;padding:0;box-sizing:border-box}
html,body{width:1200px;height:687px;overflow:hidden;background:var(--white);font-family:"Lato",sans-serif}
.page{position:relative;width:1200px;height:687px;overflow:hidden}

.site-header{position:absolute;left:0;top:0;width:1200px;height:77px;background:var(--navy);color:var(--white)}
.contact{position:absolute;left:808px;top:7px;font-size:8.5px}
.contact strong{font-weight:700}
.brand{position:absolute;left:270px;top:18px;display:flex;align-items:center;gap:7px;font-size:31px;font-weight:700;letter-spacing:-.5px}
.brand-square{width:28px;height:28px;background:var(--white);border-radius:3px}
.nav{position:absolute;top:40px;left:0;font-size:10.5px;font-weight:700}
.nav a{position:absolute;white-space:nowrap;color:var(--white);text-decoration:none}
.nav .active::after{content:"";position:absolute;left:0;right:0;top:16px;height:2px;background:var(--coral)}
.cta-partner{position:absolute;left:821px;top:33px;width:79px;height:27px;background:var(--coral);color:var(--white);font-size:10px;font-weight:700;display:flex;align-items:center;justify-content:center;white-space:nowrap}

.hero{position:absolute;left:0;top:77px;width:1200px;height:314px;background:linear-gradient(90deg,var(--wood) 0%,var(--hero-a) 8%,var(--hero-b) 50%,var(--hero-a) 92%,var(--wood) 100%)}
.hero-title{position:absolute;left:0;width:1200px;top:50px;text-align:center;color:var(--white);font-weight:900;font-size:50px;line-height:46px;letter-spacing:.5px}
.hero-sub{position:absolute;left:0;width:1200px;top:156px;text-align:center;color:var(--white);font-size:17.5px;line-height:22px}
.video-btn{position:absolute;left:513px;top:224px;width:172px;height:47px;background:var(--coral);color:var(--white);display:flex;align-items:center;justify-content:center;gap:8px;font-size:14px;letter-spacing:3.5px}
.notch{position:absolute;left:576px;top:380px;width:0;height:0;border-left:24px solid transparent;border-right:24px solid transparent;border-bottom:11px solid var(--white)}

.features{position:absolute;left:0;top:391px;width:1200px;height:119px;background:var(--white)}
.feature{position:absolute;top:25px;width:130px;margin-left:-65px;text-align:center;color:var(--navy-text)}
.feature svg{display:block;margin:0 auto 4px}
.feature p{font-size:8.5px;line-height:10.5px;font-weight:700}

.lower{position:absolute;left:0;top:510px;width:1200px;height:177px;background:linear-gradient(90deg,var(--lower-a),var(--lower-b) 40%,var(--lower-a) 100%)}
.card{position:absolute;left:277px;top:60px;width:257px;height:130px;background:var(--white);padding:20px 19px}
.card h2{color:var(--coral);font-size:12px;font-weight:700;letter-spacing:.6px;margin-bottom:10px}
.card p{color:var(--navy-text);font-size:9.8px;line-height:15.3px;margin-bottom:14px}
.card b{font-weight:700}
</style>
</head>
<body>
<div class="page">
  <header class="site-header">
    <div class="contact">Contact Sales: <strong>01632 960482</strong></div>
    <div class="brand"><span class="brand-square"></span>skydesk</div>
    <nav class="nav">
      <a class="active" style="left:498px">Home</a>
      <a style="left:542px">Hosted Desktops</a>
      <a style="left:635px">Partner Programme</a>
      <a style="left:740px">Partner Portal</a>
    </nav>
    <div class="cta-partner">Become A Partner</div>
  </header>

  <section class="hero" role="img" aria-label="Overhead photo of colleagues at a desk with tablets, charts, glasses and a laptop">
    <h1 class="hero-title">HOSTED DESKTOPS FOR<br>IT RESELLERS</h1>
    <p class="hero-sub">Get more customers, increase margins and grow your business by<br>reselling SkyDesk virtual hosted desktops.</p>
    <div class="video-btn">SHOW VIDEO
      <svg width="26" height="26" viewBox="0 0 26 26"><circle cx="13" cy="13" r="11.5" fill="none" stroke="#fff" stroke-width="2"/><path d="M10 7.5 L18.5 13 L10 18.5Z" fill="#fff"/></svg>
    </div>
    <div class="notch"></div>
  </section>

  <section class="features">
    <div class="feature" style="left:326px">
      <svg width="48" height="36" viewBox="0 0 48 36" fill="none" stroke="#16496f" stroke-width="2" stroke-linejoin="round" stroke-linecap="round"><path d="M2 12 L10 6 L18 10 L26 6 L38 6 L46 12"/><path d="M10 6 L4 22 L20 33 L30 26"/><path d="M38 6 L44 22 L32 31"/><path d="M18 10 L26 18 L30 14"/><path d="M22 30 L26 27 M26 32 L32 27"/></svg>
      <p>We only sell through<br>partners like you<br>Hosted Desktops</p>
    </div>
    <div class="feature" style="left:466px">
      <svg width="48" height="36" viewBox="0 0 48 36" fill="none" stroke="#16496f" stroke-width="2"><rect x="4" y="10" width="30" height="7"/><rect x="4" y="18" width="30" height="7"/><rect x="4" y="26" width="30" height="7"/><circle cx="36" cy="11" r="8" fill="#fff"/><path d="M32 11 L35 14 L40 8" stroke-linecap="round"/></svg>
      <p>Isolated Vireo/Stratix<br>environment<br>Revenue</p>
    </div>
    <div class="feature" style="left:602px">
      <svg width="48" height="36" viewBox="0 0 48 36" fill="none" stroke="#16496f" stroke-width="2" stroke-linecap="round" stroke-linejoin="round"><circle cx="24" cy="10" r="8"/><text x="24" y="14" text-anchor="middle" font-family="Lato,sans-serif" font-size="11" font-weight="700" fill="#16496f" stroke="none">£</text><path d="M6 26 L14 26 L22 28 L30 26 L40 20 L42 22 L32 32 L14 32"/><path d="M2 24 L6 24 L6 34 L2 34"/></svg>
      <p>Strong ongoing<br>recurring revenues<br>White Label</p>
    </div>
    <div class="feature" style="left:740px">
      <svg width="48" height="36" viewBox="0 0 48 36" fill="none" stroke="#16496f" stroke-width="2"><rect x="6" y="6" width="36" height="26"/><line x1="6" y1="11" x2="42" y2="11"/><rect x="10" y="15" width="11" height="10" fill="#16496f"/><path d="M25 16 H38 M25 20 H38 M25 24 H38"/></svg>
      <p>White label: Your brand,<br>pricing &amp; margin<br>Become a Partner</p>
    </div>
    <div class="feature" style="left:870px">
      <svg width="48" height="36" viewBox="0 0 48 36" fill="none" stroke="#16496f" stroke-width="2" stroke-linecap="round"><path d="M12 4 H32 V34 H12 Z"/><path d="M15 10 l2 2 l3-3 M23 11 H29 M15 17 l2 2 l3-3 M23 18 H29 M15 24 l2 2 l3-3 M23 25 H29"/><path d="M36 8 V28 L38 32 L40 28 V8 Z"/></svg>
      <p>No upfront fees<br>or sales commitment</p>
    </div>
  </section>

  <section class="lower" role="img" aria-label="Photo of a smiling woman working in a bright office">
    <div class="card">
      <h2>GROW YOUR REVENUE</h2>
      <p>SkyDesk's virtual hosted desktop gives you a great opportunity to resell cloud solutions under your own name and <b>using your own branding.</b></p>
      <p>Keep your customers. <b>Grow your revenue.</b></p>
    </div>
  </section>
</div>
</body>
</html>
```